One pager fact sheet for healthcare companies

We are looking for a designer to create a theme based off this example. The project will consist of building a layout and theme for a one page, front and back handout. The handout will be used as part of an educational series for medical professionals. The format must be suitable for print production. The theme should be clear, concise, and professional. Cluttered graphics will not be useable.
This project has potential to include additional work over the next 3 months.

Target Market(s)

Healthcare professionals

Industry/Entity Type

Healthcare

Font styles to use
Serif
Sans Serif

Requirements
Must have
• A professional look and feel
Should not have
• Cluttered graphics or busy look

```html
<!DOCTYPE html>
<html lang="en">
<head>
<meta charset="utf-8">
<title>Health System Fact Sheet</title>
<link href="https://fonts.googleapis.com/css2?family=Lato:ital,wght@0,400;0,700;0,900;1,400;1,700&display=swap" rel="stylesheet">
<style>
  :root {
    --cyan: #0bc3f2;
    --navy: #1f3a66;
    --navy-light: #2f5c98;
    --ink: #1d2735;
    --grey-bar: #a9abae;
    --panel: #f3f3f3;
    --band-shade: #e6e6e6;
    --field-border: #9a9a9a;
  }
  * { box-sizing: border-box; margin: 0; padding: 0; }
  html, body { width: 902px; height: 1200px; overflow: hidden; }
  body { background: #dedede; font-family: "Lato", sans-serif; color: var(--ink); position: relative; }
  .sheet { position: absolute; left: 0; top: 20px; width: 902px; height: 1161px; background: #fff; box-shadow: 0 4px 18px rgba(0,0,0,.25); }
  .abs { position: absolute; }

  /* header */
  .logo-area { left: 0; top: 0; width: 430px; height: 134px; background: #fff; }
  .logo-text { position: absolute; left: 70px; top: 52px; font-size: 28px; font-weight: 400; letter-spacing: .3px; color: var(--ink); }
  .header-divider { left: 430px; top: 0; width: 13px; height: 134px; background: var(--grey-bar); }
  .label-column { left: 443px; top: 0; width: 91px; height: 134px; background: var(--cyan); }
  .field-area { left: 534px; top: 0; width: 368px; height: 134px; background: #f1f1f1; }
  .field-label { position: absolute; left: 473px; font-size: 15px; font-weight: 700; color: var(--ink); }
  .field-box { position: absolute; left: 541px; width: 338px; background: #fff; border: 1px solid var(--field-border); }

  .stripe { position: absolute; }

  /* sections */
  .band { left: 0; width: 902px; background: linear-gradient(#ffffff, #f1f1f1); border-bottom: 2px solid var(--band-shade); }
  .side-bar { left: 0; width: 69px; background: linear-gradient(90deg, var(--navy), var(--navy-light)); display: flex; align-items: center; justify-content: center; }
  .side-bar.center { left: 432px; width: 64px; }
  .side-title { writing-mode: vertical-rl; transform: rotate(180deg); color: #fff; font-weight: 900; font-size: 17px; letter-spacing: 1.2px; text-align: center; line-height: 1.25; text-transform: uppercase; }
  .content-panel { background: #fff; }
  .content-panel.grey { background: var(--panel); }

  .block-head { position: absolute; height: 24px; background: var(--cyan); font-size: 15.5px; font-weight: 700; font-style: italic; color: var(--ink); padding-left: 8px; line-height: 24px; }
  .bullets { position: absolute; list-style: none; font-size: 12px; font-style: italic; line-height: 15px; }
  .bullets li { position: relative; padding-left: 18px; margin-bottom: 5px; }
  .bullets li::before { content: ""; position: absolute; left: 0; top: 3px; width: 9px; height: 9px; border-radius: 50%; background: var(--navy); }
  .accent { color: var(--cyan); }
  .plain-value { position: absolute; font-size: 12px; font-style: italic; }

  .distribution li { display: flex; width: 270px; }
  .distribution .leader { flex: 1; border-bottom: 1.5px dotted var(--ink); margin: 0 4px 4px 2px; }
  .distribution .pct { position: absolute; left: 280px; font-style: normal; }

  .notes-panel { left: 69px; width: 833px; background: #e4e4e4; }

  .footer { left: 0; top: 1084px; width: 598px; height: 77px; background: linear-gradient(90deg, var(--navy), var(--navy-light) 55%, var(--navy)); color: #fff; font-size: 15.5px; font-weight: 700; padding: 20px 0 0 96px; line-height: 20px; }
  .client-area { left: 598px; top: 1084px; width: 304px; height: 77px; background: #fff; }
  .client-name { position: absolute; left: 56px; top: 22px; font-size: 26px; color: var(--ink); }
</style>
</head>
<body>
<div class="sheet">

  <!-- header -->
  <div class="abs logo-area"><span class="logo-text">COMPANY LOGO</span></div>
  <div class="abs header-divider"></div>
  <div class="abs label-column"></div>
  <div class="abs field-area"></div>
  <span class="field-label" style="top:26px">Name&nbsp;&nbsp;&nbsp;:</span>
  <span class="field-label" style="top:49px">Address :</span>
  <span class="field-label" style="top:106px">Website :</span>
  <div class="field-box" style="top:25px;height:23px"></div>
  <div class="field-box" style="top:53px;height:47px"></div>
  <div class="field-box" style="top:107px;height:22px"></div>

  <div class="stripe" style="left:0;top:134px;width:203px;height:10px;background:var(--navy)"></div>
  <div class="stripe" style="left:203px;top:134px;width:227px;height:9px;background:var(--grey-bar)"></div>
  <div class="stripe" style="left:0;top:144px;width:430px;height:7px;background:var(--cyan)"></div>
  <div class="stripe" style="left:443px;top:134px;width:459px;height:10px;background:var(--navy)"></div>
  <div class="stripe" style="left:443px;top:144px;width:459px;height:7px;background:var(--cyan)"></div>
  <div class="stripe" style="left:443px;top:151px;width:459px;height:5px;background:var(--grey-bar)"></div>

  <!-- key facts / system structure -->
  <div class="abs band" style="top:156px;height:394px"></div>
  <div class="abs side-bar" style="top:167px;height:371px"><span class="side-title">Key Facts</span></div>
  <div class="abs content-panel" style="left:69px;top:167px;width:361px;height:371px"></div>
  <div class="abs side-bar center" style="top:167px;height:371px"><span class="side-title">System Structure</span></div>
  <div class="abs content-panel grey" style="left:496px;top:167px;width:406px;height:371px"></div>

  <div class="block-head" style="left:69px;top:168px;width:349px">Organization Type:</div>
  <ul class="bullets" style="left:96px;top:201px"><li>Not for Profit Health System</li></ul>

  <div class="block-head" style="left:69px;top:225px;width:349px">Leadership Team and Contact Information:</div>
  <ul class="bullets" style="left:96px;top:261px">
    <li>Helen R. Marston, CEO</li>
    <li>Daniel K. Whitford, III, President</li>
    <li>Thomas E. Callow, EVP and COO</li>
    <li>Samuel Okafor, Jr. MD, EVP and Chief Medical Officer</li>
  </ul>

  <div class="block-head" style="left:69px;top:349px;width:349px">Physicians in Network</div>
  <ul class="bullets" style="left:96px;top:385px">
    <li><span class="accent">Total:</span> 2,400 Salaried, 3,000 Affiliated</li>
    <li><span class="accent">PCPs:</span> 1,000 Salaried, 1,500 Affiliated</li>
    <li><span class="accent">Ophthalmologists:</span> 35 Salaried, 0 Affiliated</li>
    <li><span class="accent">Retina Specialists:</span> 10 Salaried, 0 Affiliated</li>
  </ul>

  <div class="block-head" style="left:69px;top:475px;width:349px">Covered Lives</div>
  <span class="plain-value" style="left:112px;top:505px">800,000</span>

  <div class="block-head" style="left:496px;top:168px;width:374px">Geographic Coverage:</div>
  <ul class="bullets" style="left:545px;top:205px"><li>Michigan</li></ul>

  <div class="block-head" style="left:496px;top:233px;width:374px">Number of Hospitals and Facilities:</div>
  <ul class="bullets" style="left:545px;top:269px;width:310px">
    <li>7 Hospitals</li>
    <li>Over 35 medical centers and facilities across multiple counties in Michigan</li>
  </ul>

  <div class="block-head" style="left:496px;top:333px;width:374px">Key Affiliations</div>
  <ul class="bullets" style="left:545px;top:370px;width:300px">
    <li>Medical Group has more than 1,100 physicians that staff Lakeview hospital, Cedar Ridge hospital, and 26 medical centers</li>
    <li>Physician Network is a physician-led subsidiary, comprising the Medical Group, hospital-employed and private practice physicians</li>
    <li>2,000 affiliated private practice physicians</li>
  </ul>

  <!-- services -->
  <div class="abs band" style="top:552px;height:196px"></div>
  <div class="abs side-bar" style="top:568px;height:178px"><span class="side-title">Services</span></div>
  <div class="abs content-panel" style="left:69px;top:568px;width:424px;height:178px"></div>
  <div class="abs" style="left:493px;top:590px;width:2px;height:130px;background:linear-gradient(transparent,#d4d4d4,transparent)"></div>

  <div class="block-head" style="left:69px;top:567px;width:349px">Key Services and Facilities</div>
  <ul class="bullets" style="left:96px;top:611px;width:310px">
    <li><span class="accent">Major service lines:</span> cardiac care, women’s and children’s services, cancer care, orthopedics, transplants, neuroscience, trauma, and urology</li>
    <li><span class="accent">Key Facilities:</span> ClearView Eye centers include offices for ophthalmologists and retina specialists</li>
  </ul>

  <div class="block-head" style="left:496px;top:567px;width:374px;padding-left:32px">Distribution of Outpatient Services</div>
  <ul class="bullets distribution" style="left:545px;top:608px">
    <li>In Facilities:<span class="leader"></span><span class="pct">40%</span></li>
    <li>In Owned Practices:<span class="leader"></span><span class="pct">30%</span></li>
    <li>In Affiliated Practices:<span class="leader"></span><span class="pct">20%</span></li>
    <li>Unaffiliated/ Out of Network:<span class="leader"></span><span class="pct">10%</span></li>
  </ul>

  <!-- payer relationships -->
  <div class="abs band" style="top:750px;height:328px"></div>
  <div class="abs side-bar" style="top:757px;height:324px"><span class="side-title">Key Payer Relationships and<br>Payment Models</span></div>
  <div class="abs content-panel" style="left:69px;top:757px;width:424px;height:160px"></div>
  <div class="abs" style="left:493px;top:775px;width:2px;height:130px;background:linear-gradient(transparent,#d4d4d4,transparent)"></div>

  <div class="block-head" style="left:69px;top:769px;width:349px">Key Plans:</div>
  <ul class="bullets" style="left:96px;top:807px">
    <li>Northgate Health</li><li>Lakeshore Shield Plan</li><li>Harborline Network</li><li>Vantora Health</li><li>Brookfield Care</li>
  </ul>
  <ul class="bullets" style="left:268px;top:807px">
    <li>Senior Care Plan</li><li>State Family Plan</li><li>Corvella</li><li>Pinecrest Health</li><li>Meridale Health</li>
  </ul>

  <div class="block-head" style="left:496px;top:769px;width:374px;padding-left:32px">Level of Risk Taken</div>
  <ul class="bullets" style="left:545px;top:811px;width:300px">
    <li>80% of revenue is billed under a risk-based payment scheme</li>
    <li>Half of these lives include the risk for outpatient, physician-administered biologics</li>
  </ul>

  <div class="abs notes-panel" style="top:917px;height:148px"></div>
  <ul class="bullets" style="left:96px;top:929px;width:745px;font-size:11.5px">
    <li>COMPANY accepts a variety of risk-based payment models including full and partial risk, bundled payments, and ACO contracts.</li>
    <li>All decisions to join an ACO or participate in a risk-based contract are made at the corporate level.</li>
    <li>COMPANY is contracted with the federal payer as an Advanced Tier ACO. Through the HMO product, this contract represents 30% of the health system’s revenue and covers over 20,000 senior plan lives.</li>
    <li>The remaining share of revenue typically includes a value-based payment model. Contracts with private payers, such as Lakeshore Shield Plan, incorporate contracts based on performance and quality of care which may lead to bonus payments.</li>
  </ul>

  <div class="stripe" style="left:143px;top:1070px;width:759px;height:7px;background:var(--grey-bar)"></div>
  <div class="stripe" style="left:598px;top:1077px;width:304px;height:7px;background:var(--cyan)"></div>

  <!-- footer -->
  <div class="abs footer"><span class="accent">Source:</span> www.company.com website pages.<br>Perceptra web survey conducted November 2016.</div>
  <div class="abs client-area"><span class="client-name">CLIENT LOGO</span></div>
</div>
</body>
</html>
```